Eye Catching Podcast Cover

My Podcast "Velvet Tracks Under Shelves" is a casual, entertaining hangout with friends telling stories, giving valuable advice, and playing great songs that otherwise would still be sitting in a database. It is not just a music podcast which is what I feel the current design communicates.
I engage and lead these artist in conversations about how to pursue any dream. The final design should communicate my unique relationship with singer/songwriters to provide valuable and applicable information on pursing a dream while hearing a uncut or released hit song.
It may just be my picture...??

Target Market(s)

Entrepreneurs, singer/songwriters

Industry/Entity Type

Entertainment

Logo Text

Velvet Tracks Under Shelves

Requirements
Must have
• My picture

```html
<!DOCTYPE html>
<html lang="en">
<head>
<meta charset="UTF-8">
<title>Velvet Tracks Under Shelves — Podcast Cover</title>
<link rel="stylesheet" href="https://fonts.googleapis.com/css2?family=Bodoni+Moda:ital,opsz,wght@0,6..96,400;1,6..96,400&family=Montserrat:wght@500&display=swap">
<style>
  :root {
    --bg-deep: #0d1220;
    --bg-mid: #1a2236;
    --ink: #ffffff;
    --gold: #9c8a2a;
    --mic-ghost: #262d3d;
    --jacket: #1d2a63;
    --skin: #d9a58c;
    --hair: #8a5a35;
  }
  * { margin: 0; padding: 0; box-sizing: border-box; }
  html, body { width: 1200px; height: 1200px; overflow: hidden; background: var(--bg-deep); }
  .cover {
    position: relative;
    width: 1200px; height: 1200px;
    background: radial-gradient(ellipse at 55% 35%, var(--bg-mid) 0%, var(--bg-deep) 70%);
    overflow: hidden;
  }
  .mic-decoration {
    position: absolute;
    left: 0; top: 200px;
    width: 150px; height: 590px;
    background: linear-gradient(180deg, var(--mic-ghost), rgba(38,45,61,0.5));
    border-radius: 0 60px 40px 0;
    opacity: 0.7;
  }
  .host-photo {
    position: absolute;
    left: 300px; top: 20px;
    width: 900px; height: 1180px;
    background:
      radial-gradient(ellipse 26% 30% at 68% 46%, var(--skin) 0%, rgba(217,165,140,0.6) 55%, transparent 100%),
      radial-gradient(ellipse 28% 16% at 66% 16%, var(--hair) 0%, rgba(138,90,53,0.5) 60%, transparent 100%),
      radial-gradient(ellipse 60% 45% at 62% 95%, var(--jacket) 0%, rgba(29,42,99,0.7) 60%, transparent 100%);
  }
  .title {
    position: absolute;
    left: 0; top: 0;
    color: var(--ink);
    font-family: "Bodoni Moda", "Didot", serif;
  }
  .title-top {
    position: absolute;
    left: 36px; top: 148px;
    font-size: 78px;
    letter-spacing: 2px;
    line-height: 1;
    white-space: nowrap;
  }
  .title-main {
    position: absolute;
    left: 22px; top: 232px;
    font-size: 154px;
    line-height: 1;
    letter-spacing: -2px;
    white-space: nowrap;
  }
  .title-rule {
    position: absolute;
    left: 79px; top: 459px;
    width: 492px; height: 2px;
    background: var(--gold);
  }
  .title-rule::after {
    content: "";
    position: absolute;
    left: 333px; top: -4px;
    width: 10px; height: 10px;
    border-radius: 50%;
    background: var(--ink);
  }
  .title-sub {
    position: absolute;
    left: 40px;
    font-style: italic;
    font-size: 104px;
    line-height: 1;
    white-space: nowrap;
  }
  .title-sub.line-1 { top: 472px; }
  .title-sub.line-2 { top: 588px; }
  .format-label {
    position: absolute;
    left: 0; width: 1200px;
    top: 1122px;
    text-align: center;
    color: var(--ink);
    font-family: "Montserrat", sans-serif;
    font-weight: 500;
    font-size: 40px;
    letter-spacing: 14px;
    padding-left: 14px;
  }
</style>
</head>
<body>
  <div class="cover">
    <div class="mic-decoration" role="img" aria-label="Faint studio microphone silhouette in the background"></div>
    <div class="host-photo" role="img" aria-label="Portrait photo of the podcast host in a navy blazer"></div>
    <div class="title">
      <div class="title-top">VELVET</div>
      <div class="title-main">TRACKS</div>
      <div class="title-rule"></div>
      <div class="title-sub line-1">under</div>
      <div class="title-sub line-2">shelves</div>
    </div>
    <div class="format-label">PODCAST</div>
  </div>
</body>
</html>
```